Mortgage Company Website / based from Corvale design

Mortgage company needs a WordPress site designed and developed using Pixel Harbor's Corvale framework. Existing site is BrantlyMortgage.example.

Goals of website:
1) Attract new leads for Home loans (first-time home buyers, people moving to Dallas, and people re-financing their homes.
2) Attract and recruit new Loan Officers.

LOAN PRODUCTS OFFERED
Conventional
Jumbo
VA
FHA
USDA
Refinance
Construction Loans - not a main product. Don't like to do these.
Remodel

Target Market(s)

Middle to upper income families in the Dallas area.

Industry/Entity Type

Mortgage Brokerage

Coding

Coded - Design and coding required

Number of Pages Required

2 page

Requirements
Must have
• Must use one of the Corvale theme from Pixel Harbor for development
https://corvale.pixel-harbor.example/

Client is focused on higher-end clientele and likes the use of the color gold.

NAVIGATION
Home Loans
Mortgage Resources
About Us
Contact Us

Site must also look good on mobile phones and tablets. Corvale theme has breakpoints already developed so should make that easier.
Nice to have
• Client likes the designs of these sites:
https://merrowfield.example/home-loans (this one was talked about as her favorite)
https://thepembrookteam.example/
https://www.servicehomeloans.example/

- Overall wants the site to be clean with lots of white space

Wants to keep the imagery focused on the families and people buying the home.

Also likes the focus on giving back to the community from the example site provided. Brantly gives to "Hearts for Hounds"

Things that can be featured on the home page:
* Hero image on top
* Top of K, Calloway Lending Champion award. Calloway 100 Mortgage Lending Champion 2020
* 3 Most recent blog posts
* Video from current homepage
* Get started form: Name, Email, Phone. Submit button
* Footer area can have navigation, contact info, and awards sections

some possible Corvale templates to choose from:
https://corvale.pixel-harbor.example/charity/
https://corvale.pixel-harbor.example/cryptocurrency/
https://corvale.pixel-harbor.example/freelancer/
https://corvale.pixel-harbor.example/finance/
https://corvale.pixel-harbor.example/financial-advisor/
https://corvale.pixel-harbor.example/university/
https://corvale.pixel-harbor.example/marketing-consultant/

```html
<!DOCTYPE html>
<html lang="en">
<head>
<meta charset="utf-8">
<title>Brantly Mortgage</title>
<link href="https://fonts.googleapis.com/css2?family=Playfair+Display:wght@700;900&family=Mulish:wght@400;600;700&display=swap" rel="stylesheet">
<style>
:root{
  --gold:#b8952c;
  --gold-light:#cfae48;
  --ink:#1c1c1c;
  --body:#6a6a6a;
  --dark:#2a2a2a;
  --footer:#1b1b1b;
  --white:#ffffff;
  --serif:'Playfair Display', serif;
  --sans:'Mulish', sans-serif;
}
*{margin:0;padding:0;box-sizing:border-box}
html,body{width:1200px;height:3189px;overflow:hidden;background:var(--white);font-family:var(--sans);color:var(--ink)}
.page{position:relative;width:1200px;height:3189px;overflow:hidden}
.abs{position:absolute}
.btn{position:absolute;background:linear-gradient(180deg,var(--gold-light),var(--gold));color:var(--white);font:700 13px var(--sans);text-transform:uppercase;display:flex;align-items:center;justify-content:center;letter-spacing:.2px}

/* hero */
.hero{position:absolute;left:0;top:0;width:1200px;height:592px;background:linear-gradient(90deg,#f6f6f4 0%,#efefec 45%,#e4e1dc 100%)}
.hero-photo{position:absolute;left:560px;top:0;width:640px;height:592px;background:radial-gradient(ellipse at 60% 45%,#d8c9bb 0%,#c9b4a3 30%,#a9b9c2 60%,#e9e7e3 100%);opacity:.85}
.brand{position:absolute;left:144px;top:22px;font:900 50px/1 var(--serif);color:var(--ink);letter-spacing:1px}
.brand-sub{position:absolute;left:146px;top:108px;font:700 11px var(--sans);letter-spacing:4px;color:var(--ink)}
.nav{position:absolute;top:56px;left:375px;display:flex;gap:27px;font:400 13px var(--sans);color:var(--ink)}
.nav .active{border-bottom:3px solid var(--gold);padding-bottom:6px}
.hero-title{position:absolute;left:144px;top:253px;font:700 54px/64px var(--serif);color:var(--ink);text-transform:uppercase}
.hero-title .gold{color:var(--gold)}
.dots{position:absolute;left:584px;top:546px;display:flex;gap:4px}
.dots i{width:7px;height:7px;border-radius:50%;background:#9a9a9a}
.dots i.on{background:var(--gold)}

/* products */
.products{position:absolute;left:0;top:592px;width:1200px;height:214px;background:linear-gradient(180deg,#4b4a4a,#1e1e1e)}
.section-title{font:700 34px var(--serif);text-transform:uppercase;text-align:center}
.products .section-title{position:absolute;top:38px;width:100%;color:var(--white)}
.arrow{position:absolute;top:120px;width:44px;height:44px;border:2px solid var(--white);border-radius:50%}
.product{position:absolute;top:116px;display:flex;align-items:center;gap:12px;color:var(--white);font:400 16px var(--sans);text-transform:uppercase}

/* welcome */
.badge{position:absolute;top:907px;width:200px;height:250px;background:#e31b23;border-top:72px solid #111}
.badge-cap{position:absolute;top:1165px;width:210px;text-align:center;font:600 11px/14px var(--sans);text-transform:uppercase;color:var(--ink)}
.welcome-title{position:absolute;left:650px;top:887px;font:700 36px/42px var(--serif);text-transform:uppercase}
.welcome-title .gold{color:var(--gold)}
.welcome-copy{position:absolute;left:650px;top:991px;width:420px;font:400 15px/27px var(--sans);color:var(--body)}

/* video & form */
.band{position:absolute;left:0;top:1440px;width:1200px}
.video{position:absolute;left:248px;top:1328px;width:704px;height:376px;background:linear-gradient(135deg,#f1f1f1,#d8d8d8)}
.play{position:absolute;left:572px;top:1490px;width:56px;height:56px;border-radius:50%;background:#e2141c}
.gs-title{position:absolute;top:1762px;width:100%;color:var(--white)}
.field{position:absolute;top:1848px;height:46px;background:var(--white);font:400 15px var(--sans);color:#777;padding-left:20px;display:flex;align-items:center}
.submit{position:absolute;left:856px;top:1848px;width:160px;height:46px;background:#262626;color:var(--white);font:700 16px var(--sans);display:flex;align-items:center;justify-content:center;text-transform:uppercase}

/* blog */
.blog-title{position:absolute;top:2082px;width:100%;color:var(--ink)}
.blog-title .gold{color:var(--gold)}
.thumb{position:absolute}
.post-title{position:absolute;font:600 16px/24px var(--sans);color:var(--ink)}
.post-meta{position:absolute;font:400 11px/18px var(--sans);color:var(--gold)}
.feature-title{position:absolute;left:144px;top:2490px;font:600 20px var(--sans)}
.feature-copy{position:absolute;left:144px;top:2572px;width:410px;font:400 13px/24px var(--sans);color:var(--body)}

/* footer */
.footer{position:absolute;left:0;top:2835px;width:1200px;height:354px;background:var(--footer);color:var(--white)}
.footer-brand{position:absolute;left:176px;top:82px;font:900 84px/1 var(--serif);color:var(--white)}
.footer-sub{position:absolute;left:184px;top:282px;font:700 20px var(--sans);letter-spacing:8px}
.charity{position:absolute;left:506px;top:78px;font:700 30px var(--sans);color:var(--white)}
.footer-nav{position:absolute;left:506px;top:147px;display:flex;gap:31px;font:400 15px var(--sans);text-transform:uppercase}
.copyright{position:absolute;left:506px;top:199px;font:400 11px var(--sans)}
.social{position:absolute;left:506px;top:255px;display:flex;gap:36px}
.social i{width:22px;height:22px;border-radius:50%;background:var(--white)}
</style>
</head>
<body>
<div class="page">

<header class="hero">
  <div class="hero-photo" role="img" aria-label="Photo of a father lifting his smiling young daughter into the air in a bright white room"></div>
  <div class="brand">Brantly</div>
  <div class="brand-sub">MORTGAGE INC</div>
  <nav class="nav">
    <span class="active">HOME LOANS</span><span>MORTGAGE RESOURCES</span><span>ABOUT US</span><span>CONTACT US</span>
  </nav>
  <div class="btn" style="left:925px;top:43px;width:130px;height:40px">Get Started</div>
  <h1 class="hero-title">The Peoples<br><span class="gold">Lender! We Make</span><br>It Happen</h1>
  <div class="btn" style="left:144px;top:473px;width:129px;height:38px">Get Started</div>
  <div class="dots"><i></i><i class="on"></i><i></i></div>
</header>

<section class="products">
  <h2 class="section-title">Loan Products</h2>
  <svg class="arrow" style="left:76px" viewBox="0 0 44 44"><path d="M25 14l-8 8 8 8" stroke="#fff" stroke-width="2.5" fill="none"/></svg>
  <div class="product" style="left:167px"><svg width="50" height="50" viewBox="0 0 50 50"><rect x="4" y="6" width="42" height="40" fill="none" stroke="#b8952c" stroke-width="2"/><path d="M10 46V22h30v24M18 30h14v16" fill="none" stroke="#b8952c" stroke-width="2"/></svg>Conventional</div>
  <div class="product" style="left:424px"><svg width="56" height="40" viewBox="0 0 56 40"><path d="M4 26c10-14 38-14 48 0-12 8-36 8-48 0zM22 14V6h12v8" fill="none" stroke="#b8952c" stroke-width="2"/></svg>Jumbo</div>
  <div class="product" style="left:630px"><svg width="56" height="40" viewBox="0 0 56 40"><path d="M4 26c10-14 38-14 48 0-12 8-36 8-48 0zM22 14V6h12v8" fill="none" stroke="#b8952c" stroke-width="2"/></svg>Refinance</div>
  <div class="product" style="left:872px"><svg width="46" height="52" viewBox="0 0 46 52"><rect x="4" y="6" width="32" height="42" fill="none" stroke="#b8952c" stroke-width="2"/><circle cx="24" cy="30" r="8" fill="none" stroke="#b8952c" stroke-width="2"/><path d="M30 36l10 10" stroke="#b8952c" stroke-width="2.5"/></svg>Refinance</div>
  <svg class="arrow" style="left:1079px" viewBox="0 0 44 44"><path d="M19 14l8 8-8 8" stroke="#fff" stroke-width="2.5" fill="none"/></svg>
</section>

<section>
  <div class="badge" style="left:144px" role="img" aria-label="Top of K award badge"></div>
  <div class="badge-cap" style="left:139px">Calloway Lending Champion Award</div>
  <div class="badge" style="left:380px" role="img" aria-label="Top of K award badge"></div>
  <div class="badge-cap" style="left:375px">Calloway 100 Mortgage Lending Champion 2020</div>
  <h2 class="welcome-title">Welcome to<br><span class="gold">Brantly</span> Mortgage</h2>
  <p class="welcome-copy">Brantly Mortgage is founded with passion and the heart of serving. We strive to keep the mortgage experience simple, efficient, and enjoyable for our clients. Brantly Mortgage is here to serve you whether you are looking for the best rates in town with a quick and easy closing, or searching for a trustworthy and experienced mortgage loan officer to guide you through your first home purchase.</p>
  <div class="btn" style="left:650px;top:1206px;width:130px;height:39px">Read More</div>
</section>

<section>
  <svg class="band" width="1200" height="566" viewBox="0 0 1200 566" role="img" aria-label="Gold band framed by dark photo triangles of smiling families">
    <rect x="0" y="77" width="1200" height="458" fill="#b8952c"/>
    <polygon points="0,8 0,565 310,565 40,77" fill="#3a3a3a"/>
    <polygon points="0,565 160,100 330,410 0,410" fill="#2b2b2b" opacity=".8"/>
    <polygon points="1200,8 1200,565 890,565 1160,77" fill="#3a3a3a"/>
    <polygon points="1200,565 1040,100 870,410 1200,410" fill="#2b2b2b" opacity=".8"/>
  </svg>
  <div class="video" role="img" aria-label="Hand drawn explainer video still about a hassle-free mortgage process"></div>
  <svg class="play" viewBox="0 0 56 56"><path d="M22 17l17 11-17 11z" fill="#fff"/></svg>
  <h2 class="section-title gs-title">Get Started</h2>
  <div class="field" style="left:184px;width:216px">Name</div>
  <div class="field" style="left:408px;width:216px">Email</div>
  <div class="field" style="left:632px;width:216px">Phone</div>
  <div class="submit">Submit</div>
</section>

<section>
  <h2 class="section-title blog-title">Recent <span class="gold">Blog</span> Posts</h2>
  <div class="thumb" style="left:144px;top:2191px;width:433px;height:277px;background:linear-gradient(135deg,#e8ecf0,#c9cfd6 60%,#b8976e)" role="img" aria-label="Wooden house model on a veterans home loan document"></div>
  <div class="feature-title">3 Benefits to Consider VA Loans</div>
  <div class="post-meta" style="left:144px;top:2535px">By Dana Rowe-Ellis • 02 Nov, 2020 • 0 Comments</div>
  <p class="feature-copy">Surprisingly, most veterans we meet assume a VA loan process will be difficult. It is not more difficult than any other loan programs; however, it requires specific documents to be signed accurately to be acceptable for VA</p>

  <div class="thumb" style="left:622px;top:2191px;width:137px;height:101px;background:linear-gradient(135deg,#eee,#bbb 60%,#8a7b6a)" role="img" aria-label="Clock face about saving money"></div>
  <div class="post-title" style="left:781px;top:2196px;width:260px">3 Tips to SAVE Money during COVID-19</div>
  <div class="post-meta" style="left:781px;top:2265px">By Dana Rowe-Ellis • 02 Nov, 2020 • 0 Comments</div>

  <div class="thumb" style="left:622px;top:2314px;width:137px;height:101px;background:linear-gradient(135deg,#a5683a,#e9e6e0 55%,#d9d4cb)" role="img" aria-label="Forbearance agreement papers on a wooden desk"></div>
  <div class="post-title" style="left:781px;top:2319px;width:260px">3 Risks considering Mortgage Forbearance</div>
  <div class="post-meta" style="left:781px;top:2388px">By Dana Rowe-Ellis • 02 Nov, 2020 • 0 Comments</div>

  <div class="thumb" style="left:622px;top:2435px;width:137px;height:101px;background:linear-gradient(135deg,#8a5a34,#c8b79a 55%,#9aa48c)" role="img" aria-label="Jar of cash savings on a wooden table"></div>
  <div class="post-title" style="left:781px;top:2440px;width:260px">3 Refinance Solutions during COVID19</div>
  <div class="post-meta" style="left:781px;top:2509px">By Dana Rowe-Ellis • 02 Nov, 2020 • 0 Comments</div>

  <div class="thumb" style="left:622px;top:2558px;width:137px;height:101px;background:linear-gradient(135deg,#6e4526,#a7764e 50%,#cfc8c0)" role="img" aria-label="House keys and a small house model on wood"></div>
  <div class="post-title" style="left:781px;top:2563px">Second Emergency Rate Cut</div>
  <div class="post-meta" style="left:781px;top:2598px">By Dana Rowe-Ellis • 19 Mar, 2020<br>0 Comments</div>

  <div class="btn" style="left:471px;top:2721px;width:258px;height:40px">View More Blog Posts</div>
</section>

<footer class="footer">
  <div class="footer-brand">Brantly</div>
  <div class="footer-sub">MORTGAGE INC</div>
  <div class="charity">Hearts for Hounds</div>
  <nav class="footer-nav"><span>Home Loans</span><span>Mortgage Resources</span><span>About Us</span><span>Contact Us</span></nav>
  <div class="copyright">Copyright ©2020 brantlymortgage. All Rights Reserved &nbsp;|&nbsp; Privacy Policy</div>
  <div class="social"><i></i><i></i><i></i><i></i><i></i><i></i></div>
</footer>

</div>
</body>
</html>
```